Business card design for a engineering company

I need a double sided business card design for my company "Verdmont Flow Solutions". The card will be used in Malaysia. Sleek and professional, with a little design flare to it.
Information to showcase:
1. Company logo
2. Name, title, phone, email address, website address
3. our products "Pumping technology, Valve & actuation, Air Moving Technology
Example:
Ravi Tanaka
Business manager
ravi.tanaka@verdmont-example.com
www.verdmont-example.com.my
- Pumping technology
- Valve & actuation
- Air moving technology
Target Market(s)
engineers, purchasing managers
Industry/Entity Type
Business
Contact Information for Business Card
Ravi Tanaka
Business manager
ravi.tanaka@verdmont-example.com
www.verdmont-example.com.my
- Pumping technology
- Valve & actuation
- Air moving technology
catch phrase : "Solving flow challenges, exceeding expectations"

```html
<!DOCTYPE html>
<html lang="en">
<head>
<meta charset="utf-8">
<title>Verdmont Flow Solutions – Business Card</title>
<link rel="stylesheet" href="https://fonts.googleapis.com/css2?family=Montserrat:wght@600&family=Arimo:wght@400&display=swap">
<style>
  :root {
    --backdrop: #e9e6e1;
    --card: #ffffff;
    --ink-dark: #1f3f4a;
    --ink-text: #2b2b2b;
    --accent: #f39a1e;
    --muted: #5d6b73;
    --shadow: rgba(0, 0, 0, 0.14);
  }
  * { box-sizing: border-box; margin: 0; padding: 0; }
  html, body { width: 1200px; height: 1200px; overflow: hidden; }
  body {
    background: var(--backdrop);
    display: flex;
    flex-direction: column;
    align-items: center;
    justify-content: center;
    gap: 60px;
    font-family: "Arimo", Arial, sans-serif;
  }
  .card {
    width: 880px;
    height: 500px;
    background: var(--card);
    box-shadow: 0 10px 30px var(--shadow);
    position: relative;
  }
  .brand {
    display: flex;
    align-items: center;
    gap: 22px;
  }
  .brand-dot {
    width: 64px;
    height: 64px;
    border-radius: 50%;
    background: var(--accent);
    flex: none;
  }
  .brand-name {
    font-family: "Montserrat", Arial, sans-serif;
    font-weight: 600;
    color: var(--ink-dark);
    font-size: 38px;
    letter-spacing: 1px;
    line-height: 1.1;
  }
  /* Front */
  .card-front .brand {
    position: absolute;
    left: 70px;
    bottom: 90px;
  }
  .contact {
    position: absolute;
    top: 60px;
    right: 60px;
    text-align: right;
  }
  .contact-name {
    font-size: 34px;
    color: var(--ink-text);
  }
  .contact-title {
    font-size: 24px;
    color: var(--accent);
    margin-top: 4px;
  }
  .contact-lines {
    list-style: none;
    margin-top: 22px;
    font-size: 19px;
    color: var(--ink-text);
    line-height: 1.75;
  }
  .contact-lines li {
    display: flex;
    justify-content: flex-end;
    align-items: center;
    gap: 12px;
  }
  .icon {
    width: 22px;
    height: 22px;
    background: var(--accent);
    display: inline-flex;
    align-items: center;
    justify-content: center;
  }
  .icon svg { width: 14px; height: 14px; }
  /* Back */
  .card-back {
    background: linear-gradient(135deg, #ffffff 40%, #eef0f1 100%);
    display: flex;
    flex-direction: column;
    align-items: center;
    justify-content: center;
    gap: 34px;
  }
  .card-back .brand-name { font-size: 50px; }
  .card-back .brand-dot { width: 84px; height: 84px; }
  .products {
    font-size: 22px;
    color: var(--muted);
    letter-spacing: 0.5px;
  }
  .products .sep { margin: 0 12px; color: var(--ink-dark); }
</style>
</head>
<body>
  <section class="card card-front" aria-label="Card front">
    <div class="contact">
      <p class="contact-name">Ravi Tanaka</p>
      <p class="contact-title">Business manager</p>
      <ul class="contact-lines">
        <li>(+6) 07 555 0142
          <span class="icon"><svg viewBox="0 0 14 14"><path d="M3 1h3l1 3-2 1a7 7 0 0 0 4 4l1-2 3 1v3a1 1 0 0 1-1 1A11 11 0 0 1 2 2a1 1 0 0 1 1-1z" fill="#fff"/></svg></span></li>
        <li>(+6) 07 555 0143
          <span class="icon"><svg viewBox="0 0 14 14"><rect x="2" y="5" width="10" height="6" fill="#fff"/><rect x="4" y="2" width="6" height="3" fill="#fff"/></svg></span></li>
        <li>ravi.tanaka@verdmont-example.com
          <span class="icon"><svg viewBox="0 0 14 14"><rect x="1.5" y="3" width="11" height="8" fill="none" stroke="#fff" stroke-width="1.5"/><path d="M1.5 3l5.5 4.5L12.5 3" fill="none" stroke="#fff" stroke-width="1.5"/></svg></span></li>
        <li>www.verdmont-example.com.my
          <span class="icon"><svg viewBox="0 0 14 14"><circle cx="7" cy="7" r="5.5" fill="none" stroke="#fff" stroke-width="1.5"/><path d="M1.5 7h11M7 1.5c-3 3-3 8 0 11M7 1.5c3 3 3 8 0 11" fill="none" stroke="#fff" stroke-width="1.2"/></svg></span></li>
      </ul>
    </div>
    <div class="brand">
      <span class="brand-dot"></span>
      <span class="brand-name">Verdmont Flow Solutions</span>
    </div>
  </section>

  <section class="card card-back" aria-label="Card back">
    <div class="brand">
      <span class="brand-dot"></span>
      <span class="brand-name">Verdmont Flow Solutions</span>
    </div>
    <p class="products">Valve &amp; actuation<span class="sep">|</span>Air moving technology</p>
  </section>
</body>
</html>
```